Modern Business Card For A Digital Advertising Company

I'll be print on the Tarn Prints Velour paper http://us.tarnprints.example/products/velour/business-cards.html
Need's to be modern and use the color palette of the logo or gray scales. I think integrating the pixelation of the logo in to the card and having it wrap from one side to the other could be interesting. My company provides ad operations, web development, and number of other services to websites around the world. You can see my website at http://www.pixelharbor.example
Contact info on the card needs to have
Dana Welloby
President
p.555.318.4406
dana@pixelharbor.example
http://www.pixelharbor.example
Doesn't necessarily need to be in that order
Target Market(s)
Website owners
Industry/Entity Type
Business
Look and feel

```html
<!DOCTYPE html>
<html lang="en">
<head>
<meta charset="utf-8">
<title>Pixel Harbor – Business Card</title>
<link rel="stylesheet" href="https://fonts.googleapis.com/css2?family=Poiret+One&display=swap">
<style>
  :root {
    --backdrop: #d9dadb;
    --card-paper: #f6f6f4;
    --card-edge: #e2e2df;
    --ink: #2b2b2b;
    --green-deep: #4f8a1f;
    --green-mid: #72b236;
    --green-light: #b9d98f;
    --green-faint: #e6efd9;
  }
  * { box-sizing: border-box; margin: 0; padding: 0; }
  html, body {
    width: 1200px;
    height: 860px;
    overflow: hidden;
    background: var(--backdrop);
    font-family: "Poiret One", sans-serif;
  }
  .canvas {
    position: relative;
    width: 1200px;
    height: 860px;
  }
  .card {
    position: absolute;
    width: 520px;
    height: 298px;
    background: var(--card-paper);
    border: 1px solid var(--card-edge);
    box-shadow: 0 6px 18px rgba(0, 0, 0, 0.18);
    overflow: hidden;
  }
  .card--front { left: 60px; top: 150px; }
  .card--back  { left: 620px; top: 410px; }

  .pixel-band {
    position: absolute;
    top: 0;
    height: 100%;
    width: 64px;
    background: linear-gradient(180deg, var(--green-deep) 0%, var(--green-mid) 45%, var(--green-light) 80%, var(--green-faint) 100%);
  }
  .card--front .pixel-band { left: 34px; }
  .card--back .pixel-band  { left: 70px; width: 58px; }

  .globe-decor {
    position: absolute;
    right: -40px;
    top: -40px;
    width: 210px;
    height: 210px;
    border-radius: 50%;
    background: radial-gradient(circle at 40% 45%, var(--green-faint) 0%, #eef3e6 55%, rgba(246, 246, 244, 0) 72%);
  }

  .brand {
    position: absolute;
    left: 140px;
    top: 92px;
    width: 200px;
    text-align: center;
  }
  .brand__mark {
    display: flex;
    align-items: center;
    justify-content: center;
    gap: 8px;
  }
  .brand__square {
    width: 16px;
    height: 16px;
    background: var(--green-mid);
  }
  .brand__name {
    font-size: 30px;
    line-height: 1;
    color: var(--green-mid);
    letter-spacing: 1px;
    text-transform: uppercase;
  }
  .brand__person {
    margin-top: 16px;
    font-size: 12px;
    line-height: 1.35;
    letter-spacing: 1.5px;
    color: var(--ink);
    text-transform: uppercase;
  }

  .contact {
    position: absolute;
    left: 175px;
    right: 20px;
    top: 80px;
    text-align: center;
    color: var(--ink);
    font-size: 19px;
    line-height: 1.3;
    letter-spacing: 2px;
    text-transform: uppercase;
  }
  .contact__email { text-transform: uppercase; }
  .web-address {
    position: absolute;
    left: 170px;
    right: 20px;
    bottom: 16px;
    text-align: center;
    font-size: 15px;
    letter-spacing: 7px;
    color: var(--ink);
  }
</style>
</head>
<body>
<main class="canvas">
  <section class="card card--front" aria-label="Card front">
    <div class="globe-decor" role="img" aria-label="Faint green pixel globe decoration"></div>
    <div class="pixel-band" role="img" aria-label="Vertical band of green pixel squares fading downward"></div>
    <div class="brand">
      <div class="brand__mark">
        <span class="brand__square"></span>
        <span class="brand__name">Pixel Harbor</span>
      </div>
      <p class="brand__person">Dana Welloby<br>President</p>
    </div>
  </section>

  <section class="card card--back" aria-label="Card back">
    <div class="pixel-band" role="img" aria-label="Vertical band of green pixel squares fading downward"></div>
    <address class="contact" style="font-style: normal;">
      <p class="contact__name">Dana Welloby</p>
      <p class="contact__title">President</p>
      <p class="contact__phone">p.555.318.4406</p>
      <p class="contact__email">dana@pixelharbor.example</p>
    </address>
    <p class="web-address">www.pixelharbor.example</p>
  </section>
</main>
</body>
</html>
```